Kleine-Entdecker-Tag Flyer
Zielgruppe
Eltern, die ihre Kinder in ihrer Entwicklung fördern möchten.
Aufgabenstellung
Wir organisieren eine Messe mit dem Thema "Kleine Entdecker Tag". Bei der Messe geht es nicht um das Lernen über Bücher (alleine) oder das Schulische, sondern die Messe soll für Eltern sein, die ihre Kinder fördern möchten durch die Behebung von Lernblockaden, Förderung der Konzentration, Kreativität, spielerisches Lernen etc. Es geht um Kinder ab ca. 4 Jahren.
Als Aussteller werden verschiedene Themen angesprochen: Kinesiologie, Logopädie, Privatschulen mit speziellem Angenbot, Schachunterricht, spielerisches Lernangebot, Kindermalen etc. , alles was darauf zielt, Kreativität und Lernen bei Kindern zu fördern.
Wir brauchen daher einen Flyer, der die Eltern anspricht. Die Messe findet am Sonntag, 9.11.2012 statt. Beginn 11 Uhr, Ende 18.00 Uhr. Ort: Lindenhalle - Ahornsaal, Felsbergweg 7, 8047 Zürich.
Das Logo wird attached. Das Format ist frei wählbar.

```html
<!DOCTYPE html>
<html lang="de">
<head>
<meta charset="utf-8">
<title>Kleine Entdecker Tag – Flyer</title>
<link rel="stylesheet" href="https://fonts.googleapis.com/css2?family=Anton&family=Arimo:wght@400;700&display=swap">
<style>
  :root {
    --orange: #ed9b0f;
    --purple: #8b0d78;
    --blue: #3aa3dc;
    --teal: #2e8c96;
    --ink: #474747;
    --paper: #ffffff;
    --stage: #e4e6e6;
  }
  * { margin: 0; padding: 0; box-sizing: border-box; }
  html, body { width: 1200px; height: 1064px; overflow: hidden; background: var(--stage); }
  .flyer {
    position: absolute; left: 221px; top: 0;
    width: 757px; height: 1064px;
    background: var(--paper);
    font-family: "Anton", Impact, sans-serif;
    color: var(--ink);
    overflow: hidden;
  }
  .top-stripes { position: absolute; left: 0; top: 0; height: 123px; display: flex; }
  .top-stripes span { width: 88px; height: 100%; }
  .brand { position: absolute; right: 32px; top: 70px; text-align: right; }
  .brand-name { font-size: 22px; color: var(--teal); letter-spacing: .5px; display: flex; align-items: center; gap: 8px; justify-content: flex-end; }
  .brand-dot { width: 14px; height: 14px; border-radius: 50%; background: var(--teal); display: inline-block; }
  .brand-url { font-family: "Arimo", Arial, sans-serif; font-size: 9px; color: var(--ink); margin-top: 4px; }
  .title { position: absolute; right: 30px; text-align: right; text-shadow: 3px 3px 4px rgba(0,0,0,.35); line-height: 1; font-weight: 400; }
  .title-main { top: 150px; font-size: 72px; }
  .title-sub { top: 238px; font-size: 62px; }
  .date-band { position: absolute; left: 0; top: 336px; width: 757px; height: 88px; display: flex; }
  .date-band .accent { width: 176px; background: var(--orange); }
  .date-band .info { flex: 1; background: var(--purple); color: #fff; padding: 4px 0 0 18px; }
  .date { font-size: 48px; line-height: 54px; text-shadow: 2px 2px 3px rgba(0,0,0,.35); }
  .venue { font-size: 19px; line-height: 24px; text-shadow: 1px 1px 2px rgba(0,0,0,.35); }
  .benefits { position: absolute; left: 36px; top: 444px; list-style: none; }
  .benefits li { font-size: 28px; line-height: 40px; height: 53px; display: flex; align-items: center; gap: 12px; text-shadow: 2px 2px 3px rgba(0,0,0,.3); }
  .benefits li::before { content: ""; width: 18px; height: 18px; border-radius: 50%; background: var(--ink); flex: none; }
  .hours { position: absolute; left: 415px; top: 434px; width: 320px; height: 150px; }
  .hours-text { position: absolute; left: 415px; top: 434px; width: 320px; height: 150px; display: flex; align-items: center; justify-content: center; color: #fff; font-size: 50px; transform: rotate(8deg); text-shadow: 2px 2px 3px rgba(0,0,0,.4); }
  .photo { position: absolute; left: 129px; top: 668px; width: 522px; height: 267px; background: radial-gradient(ellipse at center, #e9dfd4 0%, #f4efe9 55%, #ffffff 100%); }
  .web-bar { position: absolute; left: 0; top: 937px; width: 757px; height: 71px; background: var(--ink); color: #fff; font-size: 50px; display: flex; align-items: center; justify-content: center; text-shadow: 2px 2px 3px rgba(0,0,0,.4); }
  .organizer { position: absolute; left: 36px; top: 1028px; font-family: "Arimo", Arial, sans-serif; font-size: 7px; line-height: 10px; color: #333; }
  .organizer strong { display: block; }
  .bottom-stripes { position: absolute; left: 409px; top: 1008px; height: 56px; display: flex; }
  .bottom-stripes span { width: 87px; height: 100%; }
  .orange { background: var(--orange); } .purple { background: var(--purple); }
  .blue { background: var(--blue); } .teal { background: var(--teal); }
</style>
</head>
<body>
<main class="flyer">
  <div class="top-stripes"><span class="orange"></span><span class="purple"></span><span class="blue"></span><span class="teal"></span></div>

  <div class="brand">
    <div class="brand-name"><span class="brand-dot"></span>Kleine Entdecker Tag</div>
    <div class="brand-url">www.kleine-entdecker-tag.ch</div>
  </div>

  <h1 class="title title-main">Kleine Entdecker Tag</h1>
  <h2 class="title title-sub">Messe Zürich</h2>

  <section class="date-band">
    <div class="accent"></div>
    <div class="info">
      <p class="date">So. 9. November 2012</p>
      <p class="venue">in der Lindenhalle - Ahornsaal, Felsbergweg 7, 8047 Zürich</p>
    </div>
  </section>

  <ul class="benefits">
    <li>Begabungen erkennen</li>
    <li>Konzentration fördern</li>
    <li>Lernblockaden lösen</li>
    <li>Lernen entfalten</li>
  </ul>

  <svg class="hours" viewBox="0 0 320 150" aria-hidden="true">
    <polygon fill="var(--teal)" points="320,75 271,88 299,112 241,110 240,140 190,123 160,150 130,123 80,140 79,110 21,112 49,88 0,75 49,62 21,38 79,40 80,10 130,27 160,0 190,27 240,10 241,40 299,38 271,62"/>
  </svg>
  <p class="hours-text">11-18 Uhr</p>

  <div class="photo" role="img" aria-label="Foto: zwei Kinder sitzen am Boden und spielen Schach"></div>

  <div class="web-bar">www.kleine-entdecker-tag.ch</div>

  <p class="organizer"><strong>Veranstalter:</strong>Entdeckerwelt GmbH, Am Mühlebach 12, 8804 Au</p>
  <div class="bottom-stripes"><span class="teal"></span><span class="blue"></span><span class="purple"></span><span class="orange"></span></div>
</main>
</body>
</html>
```